15 feet by 50 feet Billboard Advertisement

We need to create a large billboard advertisement for hiring Truck Drivers. The size is 15 feet by 50 feet.(it is a non-illuminated sign) Our company name is Brindlow and we can use the phone number 855-7FASTJOB to have them call. Hiring truck drivers is tough and there are typically three things they care about.

1) Feeling like they aren't just a number to the company (Brindlow is small and very personal) 2) Pay/benefits (we offer some of the top pay in the industry and have benefits) 3) New trucks (we have all our teams in new equipment)

Ideas we come up with are, but I don't think they are very strong.

Truckers!
Wait A Minute!
Think About Your Future!
Call Brindlow
855-7FASTJOB

or

Stop!
Think about your future
Look!
Consider Brindlow
Listen!
Call us at 855-7FASTJOB

I've attached our logo that can be used as well. Also we want good design in the background to attract drivers.

Target Market(s)

Truck Drivers looking for work

Font styles to use
Sans Serif

Requirements
Must have
• tight message so it is easy to read and respond while going down the road. Also although it is for a 15 x 50 today, flexible to be used by similar dimension billboards .
Nice to have
• good color pallet that isn't too over the top for cost, but crisp and sharp for such a big sign.
Should not have
• To wordy or complex

```html
<!DOCTYPE html>
<html lang="en">
<head>
<meta charset="utf-8">
<title>Brindlow – Driver Recruiting Billboard</title>
<link rel="stylesheet" href="https://fonts.googleapis.com/css2?family=Michroma&family=Oswald:wght@600;700&family=Roboto:ital,wght@1,900&display=swap">
<style>
  :root {
    --backdrop: #72bcfb;
    --panel-black: #000000;
    --paper-white: #ffffff;
    --sign-yellow: #f5e80c;
    --sign-red: #e3161c;
    --name-ink: #1e1e1e;
  }
  * { margin: 0; padding: 0; box-sizing: border-box; }
  html, body {
    width: 1200px;
    height: 881px;
    overflow: hidden;
    background: var(--backdrop);
  }
  .billboard {
    position: absolute;
    left: 40px;
    top: 262px;
    width: 1120px;
    height: 346px;
    display: flex;
    box-shadow: 0 6px 18px rgba(0, 0, 0, 0.18);
  }
  .brand-side {
    width: 460px;
    height: 100%;
    background: var(--paper-white);
    display: flex;
    flex-direction: column;
  }
  .brand-lockup {
    height: 132px;
    display: flex;
    align-items: center;
    justify-content: center;
  }
  .brand-name {
    display: flex;
    align-items: center;
    gap: 14px;
    font-family: "Oswald", sans-serif;
    font-weight: 700;
    font-size: 56px;
    line-height: 1;
    color: var(--name-ink);
    text-transform: uppercase;
  }
  .brand-mark {
    width: 28px;
    height: 28px;
    border-radius: 50%;
    background: var(--name-ink);
  }
  .road-photo {
    flex: 1;
    background:
      linear-gradient(180deg, #8e9aa6 0%, #c9cfd3 38%, #f3c25a 54%, #d88a2c 60%, #7a7f85 72%, #4d5257 100%);
  }
  .message-side {
    flex: 1;
    height: 100%;
    background: var(--panel-black);
    position: relative;
    text-align: center;
  }
  .headline {
    position: absolute;
    top: 36px;
    left: 0;
    right: 0;
    font-family: "Michroma", sans-serif;
    font-weight: 400;
    font-size: 56px;
    letter-spacing: 0.16em;
    line-height: 1;
    color: var(--sign-yellow);
    text-transform: uppercase;
  }
  .subhead {
    position: absolute;
    top: 104px;
    left: 0;
    right: 0;
    font-family: "Oswald", sans-serif;
    font-weight: 700;
    font-size: 66px;
    line-height: 1;
    color: var(--sign-red);
    transform: scaleX(0.88);
  }
  .tagline {
    position: absolute;
    top: 194px;
    left: 0;
    right: 0;
    font-family: "Michroma", sans-serif;
    font-size: 23px;
    letter-spacing: 0.1em;
    line-height: 1;
    color: var(--sign-yellow);
    text-transform: uppercase;
  }
  .call-bar {
    position: absolute;
    left: 0;
    right: 0;
    top: 238px;
    height: 68px;
    display: flex;
  }
  .call-prompt {
    width: 50%;
    background: var(--sign-red);
    display: flex;
    align-items: center;
    justify-content: center;
    font-family: "Roboto", sans-serif;
    font-style: italic;
    font-weight: 900;
    font-size: 33px;
    color: var(--sign-yellow);
  }
  .call-number {
    flex: 1;
    background: var(--sign-yellow);
    clip-path: polygon(3% 0, 100% 0, 100% 100%, 0 100%);
    margin-left: -14px;
    display: flex;
    align-items: center;
    justify-content: center;
    font-family: "Oswald", sans-serif;
    font-weight: 700;
    font-size: 46px;
    color: var(--sign-red);
  }
</style>
</head>
<body>
  <main class="billboard">
    <section class="brand-side">
      <div class="brand-lockup">
        <div class="brand-name"><span class="brand-mark"></span>Brindlow</div>
      </div>
      <div class="road-photo" role="img" aria-label="Photo of a red semi truck driving toward the viewer on an open highway at sunset"></div>
    </section>
    <section class="message-side">
      <h1 class="headline">Truckers!</h1>
      <h2 class="subhead">Wait A Minute!</h2>
      <p class="tagline">Think About Your Future!</p>
      <div class="call-bar">
        <div class="call-prompt">Call BRINDLOW</div>
        <div class="call-number">855-7FASTJOB</div>
      </div>
    </section>
  </main>
</body>
</html>
```